Harvest Lantern Ministry Conference

I am in need of promotional graphics for our upcoming event. This event, titled "Harbor Crest Youth Conference", is a weekend event for teenagers 11-19 years old. They hear from religious speakers, listen to a band, and do other fun activities. Graphic design should be geared to young adults/older teens. Alcohol, drugs, smoking are not permitted. Open to any color combinations you think fit with your design.
Event Info:
November 1-3, 2024
Tellwood Exhibit Hall, Sioux Falls, SD
Speakers: Marcus Linden (man in light blue shirt in attached photo), Tessa Vandermeer (woman in attached photo), Colin Hardy ( man in dark colored shirt in attached photo)
Worship: KW Collective
HarborCrestGather.com
#742GR
Our Organization Logo (attached): Lumenward
Once designed, I need the following graphics file sizes:
-11x17 Vertical Poster design: include all event info AND a "blank" space on the bottom or box for groups to add their own details/information. Also include the QRV logo and our organization logo Lumenward in some way.
-Make an additional copy of the 11x17 pdf with cut and bleed lines for printing, please.
-4x3 horizontal postcard: include all event info on 1 side including Lumenward logo and QRV; blank backside
-Main Graphic Slide: formatted to fit a widescreen 16x9 screen. Include event name, hashtag, QRV and Lumenward logo
-social media graphic(s) for event: can incorporate some or all of the event details. WILLING TO ADJUST BUDGET FOR SOCIAL MEDIA graphics.
-4.25in x 2.75in vertical badge: include event title on front with Lumenward logo
Target Market
ages 11-19
Target Market(s)
11-19 years old
Industry/Entity Type
Christian Youth Ministry

```html
<!DOCTYPE html>
<html lang="en">
<head>
<meta charset="utf-8">
<title>Harbor Crest Youth Conference – Flyer</title>
<link href="https://fonts.googleapis.com/css2?family=Cinzel:wght@400;600&family=Great+Vibes&family=Arimo:wght@700&display=swap" rel="stylesheet">
<style>
  :root{
    --stage:#807f80;
    --paper:#f7f7f7;
    --paper-shade:#ececec;
    --dark-1:#2a1d17;
    --dark-2:#4a3426;
    --dark-3:#6b4a33;
    --gold-light:#fff07a;
    --gold:#e2b70f;
    --gold-deep:#8a6400;
    --ink:#3c3c3c;
    --ink-soft:#5a5a5a;
    --white:#ffffff;
    --photo-warm:#cfc3b6;
    --photo-cool:#7fa6c2;
    --photo-dusk:#5b4b45;
  }
  *{box-sizing:border-box;margin:0;padding:0}
  html,body{width:1200px;height:800px;overflow:hidden;background:var(--stage)}
  .stage{position:relative;width:1200px;height:800px}
  .flyer{
    position:absolute;left:310px;top:25px;width:580px;height:750px;
    background:var(--paper);overflow:hidden;
    box-shadow:0 10px 30px rgba(0,0,0,.25);
  }
  .flyer__backdrop{position:absolute;inset:0}
  .flyer__shade{position:absolute;left:0;top:520px;width:330px;height:230px;background:var(--paper-shade)}
  .brand{
    position:absolute;left:34px;top:44px;display:flex;align-items:center;gap:8px;
    padding:10px 12px;background:rgba(255,255,255,.08);
  }
  .brand__mark{width:12px;height:12px;background:var(--white)}
  .brand__name{font-family:'Cinzel',serif;font-weight:600;font-size:15px;color:var(--white);letter-spacing:1px}
  .title{position:absolute;left:0;top:95px;width:580px}
  .title__line{
    display:block;font-family:'Cinzel',serif;font-weight:400;font-size:86px;line-height:.82;
    background:linear-gradient(180deg,var(--gold-light) 0%,var(--gold) 45%,var(--gold-deep) 100%);
    -webkit-background-clip:text;background-clip:text;color:transparent;
    filter:drop-shadow(2px 3px 2px rgba(0,0,0,.6));
    letter-spacing:-2px;
  }
  .title__line--1{padding-left:92px}
  .title__line--2{padding-left:118px}
  .title__line--3{padding-left:108px}
  .title__script{
    display:block;font-family:'Great Vibes',cursive;font-size:118px;line-height:1;
    color:var(--white);margin:-58px 0 0 70px;
    text-shadow:1px 2px 3px rgba(0,0,0,.4);
  }
  .speakers{position:absolute;left:44px;top:470px}
  .speakers__label{font-family:'Cinzel',serif;font-size:17px;color:var(--ink-soft);letter-spacing:1px}
  .speaker{position:absolute;width:120px}
  .speaker__photo{display:block;width:120px;height:100px}
  .speaker__name{
    display:block;margin-top:6px;padding-left:6px;border-left:2px solid var(--ink);
    font-family:'Arimo',sans-serif;font-weight:700;font-size:10px;text-transform:uppercase;color:var(--ink);
  }
  .speaker--1{left:80px;top:505px}
  .speaker--2{left:250px;top:470px}
  .speaker--3{left:410px;top:430px}
  .details{position:absolute;left:62px;top:636px}
  .details__date{font-family:'Cinzel',serif;font-size:36px;color:var(--gold);letter-spacing:1px;line-height:1}
  .details__line{font-family:'Cinzel',serif;font-size:19px;color:var(--ink-soft);letter-spacing:1px;margin-top:6px}
</style>
</head>
<body>
<div class="stage">
  <article class="flyer">
    <svg class="flyer__backdrop" width="580" height="750" viewBox="0 0 580 750" role="img" aria-label="Dim worship photo of a person holding an open book with warm bokeh lights">
      <defs>
        <linearGradient id="backdropTone" x1="0" y1="0" x2="1" y2="1">
          <stop offset="0" stop-color="var(--dark-3)"/>
          <stop offset=".45" stop-color="var(--dark-2)"/>
          <stop offset="1" stop-color="var(--dark-1)"/>
        </linearGradient>
      </defs>
      <path d="M0 0H580V400H515V478L432 462H330V520H0Z" fill="url(#backdropTone)"/>
    </svg>
    <div class="flyer__shade"></div>

    <div class="brand">
      <span class="brand__mark"></span>
      <span class="brand__name">Lumenward</span>
    </div>

    <h1 class="title">
      <span class="title__line title__line--1">HARBOR</span>
      <span class="title__line title__line--2">CREST</span>
      <span class="title__line title__line--3">YOUTH</span>
      <span class="title__script">Conference</span>
    </h1>

    <p class="speakers"><span class="speakers__label">SPEAKERS -</span></p>

    <figure class="speaker speaker--1">
      <svg class="speaker__photo" viewBox="0 0 120 100" role="img" aria-label="Portrait of speaker Marcus Linden"><rect width="120" height="100" fill="var(--photo-cool)"/></svg>
      <figcaption class="speaker__name">Marcus Linden</figcaption>
    </figure>
    <figure class="speaker speaker--2">
      <svg class="speaker__photo" viewBox="0 0 120 100" role="img" aria-label="Portrait of speaker Tessa Vandermeer"><rect width="120" height="100" fill="var(--photo-warm)"/></svg>
      <figcaption class="speaker__name">Tessa Vandermeer</figcaption>
    </figure>
    <figure class="speaker speaker--3">
      <svg class="speaker__photo" viewBox="0 0 120 100" role="img" aria-label="Portrait of speaker Colin Hardy"><rect width="120" height="100" fill="var(--photo-dusk)"/></svg>
      <figcaption class="speaker__name">Colin Hardy</figcaption>
    </figure>

    <div class="details">
      <p class="details__date">NOVEMBER 1-3, 2024</p>
      <p class="details__line">WORSHIP: KW COLLECTIVE</p>
      <p class="details__line">HARBORCRESTGATHER.COM &nbsp;#742GR</p>
    </div>
  </article>
</div>
</body>
</html>
```